A start-up named "Corvath Therapeutics" - needs a new PowerPoint design

We need a new PowerPoint Design for an early-stage start-up named "Corvath Therapeutics" seeking to disrupt the current approach towards drug discovery within aging disorders.

We would like to build on Corvath's legacy, the founder of the modern science of genetics, by employing a multidisciplinary approach, experimenting, and providing elderly patients the attention they deserve.

We have selected the suffix "therapeutics" intentionally as it stands for (a medicine) the treatment of disease; the science of healing. Alzheimer’s treatment is a huge, urgent, unmet need:
- Shift from a disease-management system to a preventive medicine system
- Focus on increasing the health span, not only the life span

Target Market(s)

Pharma/ Biotech Executives Medical Institutions Healthcare professionals (MDs, nurses, payors, pharmacists, etc.) Patients

Industry/Entity Type

Healthcare

Other font styles liked:
• Celias

Colors
0054AA
0677BA
7BADD7
CADEEF
E8F1F8
E54698
E96AAD
F1A4CE
F9D9EA
FCEFF6
A7469A
B969AE
D3A5CF
EDDBEB
F8F0F9
6B429C
8869AF
B7A5CE
E3DAEB
F3F0F8

Requirements
Must have
• - differentiate from other companies named after Corvath - differentiate from other Pharma/ Biotech companies
Nice to have
• simplicity/ minimalist logo vivid colors gradient 3D Life-Sciences inspired Simple geometry Balance
Should not have
• mascot/ emblem watermark logo animated ink style nature-inspired inventive typography artistic chaos

```html
<!DOCTYPE html>
<html lang="en">
<head>
<meta charset="utf-8">
<title>Corvath Therapeutics – Presentation Template</title>
<link href="https://fonts.googleapis.com/css2?family=Outfit:wght@300;400;500;600;700&display=swap" rel="stylesheet">
<style>
:root{
  --blue:#2a9fd8;
  --blue-deep:#0054aa;
  --navy:#2b3990;
  --magenta:#c2238c;
  --pink:#e54698;
  --purple:#6b429c;
  --text:#6d6d72;
  --page:#ffffff;
  --sky:#7badd7;
}
*{margin:0;padding:0;box-sizing:border-box}
html,body{width:1200px;height:2194px;overflow:hidden;background:var(--page)}
body{font-family:"Outfit",sans-serif;position:relative}
.slide{position:absolute;width:541px;height:305px;background:#fff;overflow:hidden;box-shadow:0 6px 22px rgba(0,0,0,.16)}
.col-l{left:43px}.col-r{left:614px}
.ph{position:absolute}
.abs{position:absolute}
.brand{position:absolute;display:flex;align-items:center;gap:4px;font-weight:500;font-size:10px;color:var(--navy);line-height:1}
.brand .dot{width:9px;height:9px;background:var(--blue)}
.h2{position:absolute;color:var(--blue);font-weight:500;font-size:15px;line-height:1.15}
.caps{text-transform:uppercase;font-weight:600}
.sub{position:absolute;color:var(--magenta);font-weight:600;font-size:7.5px}
.body{position:absolute;color:var(--text);font-size:5px;line-height:1.6;text-align:justify;font-weight:300;overflow:hidden}
.bullets{position:absolute;list-style:none;color:var(--pink);font-size:7px;line-height:1.4}
.bullets li{padding-left:10px;position:relative;margin-bottom:3px}
.bullets li::before{content:"";position:absolute;left:1px;top:3.5px;width:2.5px;height:2.5px;border-radius:50%;background:var(--pink)}
.bullets.bold{color:var(--magenta);font-weight:600}
.num{position:absolute;width:22px;height:22px;background:var(--navy);color:#fff;font-size:6px;display:flex;align-items:center;justify-content:center}
.cap{position:absolute;color:var(--magenta);font-weight:600;font-size:7.5px;text-align:center}
.name{position:absolute;color:var(--navy);font-weight:600;font-size:8px;text-align:center}
.role{position:absolute;color:var(--pink);font-size:5px;font-style:italic;text-align:center}
.foot{position:absolute;left:37px;top:283px;width:470px;height:8px;background:linear-gradient(90deg,var(--blue-deep),var(--blue) 60%,var(--sky));color:#fff;font-size:4.5px;display:flex;justify-content:space-between;align-items:center;padding:0 6px 0 9px}
.foot::after{content:"";position:absolute;left:0;bottom:-2px;width:100%;height:1px;background:var(--blue)}
/* photo palettes */
.p-lab{background:linear-gradient(160deg,#c9ccd0,#8d9aa0 55%,#5c8e86)}
.p-run{background:linear-gradient(160deg,#6f8a3f,#3f5a2e 50%,#c9b29a)}
.p-glove{background:linear-gradient(150deg,#2b2f3a,#1d5cb8 55%,#d7d7dc)}
.p-dish{background:linear-gradient(150deg,#d6d6d2,#b8b0aa 50%,#c8485a)}
.p-sci{background:linear-gradient(160deg,#2e2e2e,#4a3a30 45%,#e9e9ec)}
.p-paint{background:linear-gradient(135deg,#f09a3e,#e4a76a 40%,#3b8fb0 70%,#1c5c86)}
.p-yoga{background:linear-gradient(160deg,#8a6b5a,#e4662e 50%,#b8b8c4)}
.p-artist{background:linear-gradient(150deg,#c98a4e,#8c8378 45%,#4a5a56)}
.p-couple{background:linear-gradient(150deg,#d8dad6,#7f8a7a 50%,#2f4a3a)}
</style>
</head>
<body>

<!-- Slide 1 : cover -->
<section class="slide col-l" style="top:93px">
  <div class="ph" role="img" aria-label="Two runners on a forest path under a blue-to-magenta colour wash" style="inset:0;background:linear-gradient(100deg,#3aa5d8 0%,#8a5aa8 35%,#c93a95 55%,#b0508a 75%,#7a6a5a 100%)"></div>
  <div class="brand" style="left:56px;top:110px;color:#fff;font-size:26px;font-weight:400;gap:8px"><span class="dot" style="width:24px;height:24px;background:#fff"></span>Corvath</div>
  <div class="abs" style="left:88px;top:135px;color:#fff;font-size:11px;letter-spacing:1.3px;font-weight:300">Therapeutics</div>
  <p class="abs" style="left:58px;top:164px;color:#fff;font-size:16.5px;line-height:1.22;font-weight:300">Focus on <b style="font-weight:600">increasing</b><br><b style="font-weight:600">the health span,</b> not<br>only the life span</p>
</section>

<!-- Slide 2 : About -->
<section class="slide col-r" style="top:93px">
  <div class="brand" style="left:39px;top:9px"><span class="dot"></span>Corvath</div>
  <h2 class="h2" style="left:42px;top:61px">About Corvath<br>Therapeutics</h2>
  <p class="sub" style="left:42px;top:112px">You could include a subtitle here</p>
  <p class="body" style="left:42px;top:133px;width:179px;height:130px">Lorem Ipsum is simply dummy text of the printing and typesetting industry. Lorem Ipsum has been the industry's standard dummy text ever since the 1500s, when an unknown printer took a galley of type and scrambled it to make a type specimen book. It has survived not only five centuries, but also the leap into electronic typesetting, remaining essentially unchanged. It is a long established fact that a reader will be distracted by the readable content of a page when looking at its layout. The point of using Lorem Ipsum is that it has a more-or-less normal distribution of letters, as opposed</p>
  <ul class="bullets" style="left:240px;top:48px;width:120px"><li>Lorem Ipsum is simply dummy text</li><li>Dummy text ever since 1500s</li><li>Readable content</li></ul>
  <div class="ph p-lab" role="img" aria-label="Scientist working at a laboratory bench" style="left:240px;top:127px;width:123px;height:136px"></div>
  <div class="ph p-run" role="img" aria-label="Two runners on a wooded trail" style="left:380px;top:41px;width:122px;height:223px"></div>
  <div class="foot"><span>© 2021 Corvath Therapeutics. All rights reserved</span><span>Page / 2</span></div>
</section>

<!-- Slide 3 : Three images -->
<section class="slide col-l" style="top:433px">
  <div class="ph p-dish" role="img" aria-label="Culture dishes with red medium" style="left:38px;top:40px;width:114px;height:106px"></div>
  <div class="ph p-glove" role="img" aria-label="Gloved hand pipetting into a sample tray" style="left:38px;top:158px;width:114px;height:106px"></div>
  <div class="brand" style="left:168px;top:40px"><span class="dot"></span>Corvath</div>
  <h2 class="h2" style="left:172px;top:70px">Three images plus text</h2>
  <ul class="bullets" style="left:172px;top:98px;font-size:6.5px"><li>Lorem Ipsum is simply dummy text</li><li>Dummy text ever since 1500s</li></ul>
  <p class="body" style="left:172px;top:136px;width:177px;height:128px">Lorem Ipsum is simply dummy text of the printing and typesetting industry. Lorem Ipsum has been the industry's standard dummy text ever since the 1500s, when an unknown printer took a galley of type and scrambled it to make a type specimen book. It has survived not only five centuries, but also the leap into electronic typesetting, remaining essentially unchanged. It is a long established fact that a reader will be distracted by the readable content of a page when looking at its layout. Lorem Ipsum is simply dummy text of the printing and typesetting industry. Lorem Ipsum has been the industry's standard dummy text ever since the 1500s.</p>
  <div class="ph p-sci" role="img" aria-label="Researcher in a lab coat beside a microscope" style="left:366px;top:40px;width:137px;height:225px"></div>
  <div class="foot"><span>© 2021 Corvath Therapeutics. All rights reserved</span><span>Page / 3</span></div>
</section>

<!-- Slide 4 : One image -->
<section class="slide col-r" style="top:433px">
  <div class="brand" style="left:434px;top:10px"><span class="dot"></span>Corvath</div>
  <div class="ph p-paint" role="img" aria-label="Abstract fluid paint texture in orange and blue" style="left:40px;top:40px;width:206px;height:224px"></div>
  <h2 class="h2" style="left:274px;top:43px">One images plus text</h2>
  <p class="sub" style="left:274px;top:70px">You could include a subtitle here</p>
  <p class="body" style="left:274px;top:89px;width:223px;height:48px">Lorem ipsum dolor sit amet, consectetur adipiscing elit, sed do eiusmod tempor incididunt ut labore et dolore magna aliqua. Lacus sed viverra tellus in hac habitasse platea dictumst. Rutrum tellus pellentesque eu tincidunt tortor aliquam. Nisl suscipit adipiscing bibendum est ultricies integer</p>
  <p class="body" style="left:274px;top:157px;width:223px;height:100px">Lorem Ipsum is simply dummy text of the printing and typesetting industry. Lorem Ipsum has been the industry's standard dummy text ever since the 1500s, when an unknown printer took a galley of type and scrambled it to make a type specimen book. It has survived not only five centuries, but also the leap into electronic typesetting, remaining essentially unchanged. It is a long established fact that a reader will be distracted by the readable content of a page when looking at its layout. Lorem Ipsum is simply dummy text of the printing and typesetting industry. Lorem Ipsum has been the industry's standard dummy text ever since the 1500s.</p>
  <div class="foot"><span>© 2021 Corvath Therapeutics. All rights reserved</span><span>Page / 4</span></div>
</section>

<!-- Slide 5 : Two images -->
<section class="slide col-l" style="top:774px">
  <div class="brand" style="left:434px;top:10px"><span class="dot"></span>Corvath</div>
  <div class="ph p-yoga" role="img" aria-label="People stretching in an exercise class" style="left:39px;top:47px;width:121px;height:150px"></div>
  <div class="ph p-lab" role="img" aria-label="Scientist handling samples in a fume hood" style="left:177px;top:47px;width:121px;height:150px"></div>
  <p class="cap" style="left:39px;top:208px;width:121px">Your title slide here</p>
  <p class="cap" style="left:177px;top:208px;width:121px">Your title slide here</p>
  <p class="body" style="left:39px;top:221px;width:121px;height:40px">Lorem ipsum dolor sit amet, consectetur adipiscing elit, sed do eiusmod tempor incididunt ut labore et dolore magna aliqua.</p>
  <p class="body" style="left:177px;top:221px;width:121px;height:40px">Lorem ipsum dolor sit amet, consectetur adipiscing elit, sed do eiusmod tempor incididunt ut labore et dolore magna aliqua.</p>
  <h2 class="h2" style="left:319px;top:51px">Two images plus text</h2>
  <div class="num" style="left:315px;top:88px">I</div>
  <div class="num" style="left:315px;top:134px">II</div>
  <div class="num" style="left:315px;top:181px">III</div>
  <div class="num" style="left:315px;top:227px">IV</div>
  <p class="body" style="left:345px;top:88px;width:153px;height:28px;text-align:left">Lorem ipsum dolor sit amet, consectetur adipiscing elit, sed do eiusmod tempor incididunt ut labore et dolore magna aliqua.</p>
  <p class="body" style="left:345px;top:134px;width:153px;height:28px;text-align:left">Lorem ipsum dolor sit amet, consectetur adipiscing elit, sed do eiusmod tempor incididunt ut labore et dolore magna aliqua.</p>
  <p class="body" style="left:345px;top:181px;width:153px;height:28px;text-align:left">Lorem ipsum dolor sit amet, consectetur adipiscing elit, sed do eiusmod tempor incididunt ut labore et dolore magna aliqua.</p>
  <p class="body" style="left:345px;top:227px;width:153px;height:28px;text-align:left">Lorem ipsum dolor sit amet, consectetur adipiscing elit, sed do eiusmod tempor incididunt ut labore et dolore magna aliqua.</p>
  <div class="foot"><span>© 2021 Corvath Therapeutics. All rights reserved</span><span>Page / 5</span></div>
</section>

<!-- Slide 6 : What we do -->
<section class="slide col-r" style="top:774px">
  <div class="brand" style="left:434px;top:10px"><span class="dot"></span>Corvath</div>
  <h2 class="h2 caps" style="left:40px;top:38px">What we do?</h2>
  <p class="body" style="left:40px;top:60px;width:172px;height:56px;font-size:7px;line-height:1.55;color:#555">Lorem ipsum dolor sit amet, consectetur adipiscing elit, sed do eiusmod tempor incididunt ut labore et dolore magna aliqua. Lacus sed viverra tellus in hac habitasse</p>
  <p class="sub" style="left:40px;top:123px">Your subtitle slide here</p>
  <p class="body" style="left:40px;top:136px;width:172px;height:42px">Lorem ipsum dolor sit amet, consectetur adipiscing elit, sed do eiusmod tempor incididunt ut labore et dolore magna aliqua. Lacus sed viverra tellus in hac habitasse platea dictumst. Rutrum tellus pellentesque eu tincidunt</p>
  <p class="sub" style="left:40px;top:195px">Your subtitle slide here</p>
  <p class="body" style="left:40px;top:208px;width:172px;height:42px">Lorem ipsum dolor sit amet, consectetur adipiscing elit, sed do eiusmod tempor incididunt ut labore et dolore magna aliqua. Lacus sed viverra tellus in hac habitasse platea dictumst. Rutrum tellus pellentesque eu tincidunt</p>
  <div class="ph p-run" role="img" aria-label="Two runners on a wooded trail" style="left:229px;top:39px;width:130px;height:225px"></div>
  <div class="ph p-glove" role="img" aria-label="Gloved hand holding a pipette over a sample tray" style="left:372px;top:39px;width:130px;height:225px"></div>
  <div class="foot"><span>© 2021 Corvath Therapeutics. All rights reserved</span><span>Page / 6</span></div>
</section>

<!-- Slide 7 : Vision -->
<section class="slide col-l" style="top:1114px">
  <div class="brand" style="left:434px;top:10px"><span class="dot"></span>Corvath</div>
  <h2 class="h2 caps" style="left:42px;top:40px">Our vision</h2>
  <p class="body" style="left:149px;top:43px;width:353px;height:64px">Lorem Ipsum is simply dummy text of the printing and typesetting industry. Lorem Ipsum has been the industry's standard dummy text ever since the 1500s, when an unknown printer took a galley of type and scrambled it to make a type specimen book. It has survived not only five centuries, but also the leap into electronic typesetting, remaining essentially unchanged. It is a long established fact that a reader will be distracted by the readable content of a page when looking at its layout. Lorem Ipsum is simply dummy text of the printing and typesetting industry. Lorem Ipsum has been the industry's standard dummy text ever since the 1500s.</p>
  <div class="ph p-artist" role="img" aria-label="Older painter at work in an outdoor studio" style="left:43px;top:112px;width:458px;height:134px"></div>
  <div class="foot"><span>© 2021 Corvath Therapeutics. All rights reserved</span><span>Page / 7</span></div>
</section>

<!-- Slide 8 : Missions -->
<section class="slide col-r" style="top:1114px">
  <div class="brand" style="left:39px;top:36px"><span class="dot"></span>Corvath</div>
  <h2 class="h2 caps" style="left:42px;top:68px">Our missions</h2>
  <p class="body" style="left:42px;top:94px;width:143px;height:160px">Lorem Ipsum is simply dummy text of the printing and typesetting industry. Lorem Ipsum has been the industry's standard dummy text ever since the 1500s, when an unknown printer took a galley of type and scrambled it to make a type specimen book. It has survived not only five centuries, but also the leap into electronic typesetting, remaining essentially unchanged. It is a long established fact that a reader will be distracted by the readable content of a page when looking at its layout. Lorem Ipsum is simply dummy text of the printing and typesetting industry. Lorem Ipsum has been the industry's standard dummy text ever since the 1500s.</p>
  <div class="ph p-run" role="img" aria-label="Two runners on a wooded trail" style="left:207px;top:35px;width:83px;height:158px"></div>
  <div class="ph p-artist" role="img" aria-label="Older painter working at a table" style="left:312px;top:35px;width:83px;height:158px"></div>
  <div class="ph p-glove" role="img" aria-label="Gloved hand with a pipette" style="left:419px;top:35px;width:83px;height:158px"></div>
  <p class="cap" style="left:207px;top:198px;width:83px">Mission One</p>
  <p class="cap" style="left:312px;top:198px;width:83px">Mission Two</p>
  <p class="cap" style="left:419px;top:198px;width:83px">Mission Three</p>
  <p class="body" style="left:212px;top:212px;width:75px;height:38px">Lorem Ipsum is simply dummy text of the printing and typesetting industry.</p>
  <p class="body" style="left:317px;top:212px;width:75px;height:38px">Lorem Ipsum is simply dummy text of the printing and typesetting industry.</p>
  <p class="body" style="left:424px;top:212px;width:75px;height:38px;text-align:left">Lorem Ipsum is simply dummy text of the printing and typesetting industry.</p>
  <div class="foot"><span>© 2021 Corvath Therapeutics. All rights reserved</span><span>Page / 8</span></div>
</section>

<!-- Slide 9 : Title slide -->
<section class="slide col-l" style="top:1455px">
  <div class="brand" style="left:434px;top:10px"><span class="dot"></span>Corvath</div>
  <div class="ph p-lab" role="img" aria-label="Scientist working in a fume hood" style="left:40px;top:40px;width:119px;height:180px"></div>
  <div class="ph p-glove" role="img" aria-label="Gloved hand pipetting into a sample tray" style="left:189px;top:40px;width:119px;height:180px"></div>
  <p class="cap" style="left:40px;top:231px;width:119px">Your subtitle slide here</p>
  <p class="cap" style="left:189px;top:231px;width:119px">Your subtitle slide here</p>
  <p class="body" style="left:42px;top:243px;width:119px;height:20px;text-align:left">Lorem Ipsum is simply dummy text of the printing and typesetting industry.</p>
  <p class="body" style="left:191px;top:243px;width:119px;height:20px;text-align:left">Lorem Ipsum is simply dummy text of the printing and typesetting industry.</p>
  <h2 class="h2 caps" style="left:326px;top:43px">Your title slide</h2>
  <ul class="bullets bold" style="left:326px;top:72px;font-size:7.5px"><li>Lorem Ipsum is simply dummy text</li><li>Dummy text ever since 1500s</li><li>Readable content</li></ul>
  <p class="body" style="left:326px;top:128px;width:172px;height:130px">Lorem Ipsum is simply dummy text of the printing and typesetting industry. Lorem Ipsum has been the industry's standard dummy text ever since the 1500s, when an unknown printer took a galley of type and scrambled it to make a type specimen book. It has survived not only five centuries, but also the leap into electronic typesetting, remaining essentially unchanged. It is a long established fact that a reader will be distracted by the readable content of a page when looking at its layout. Lorem Ipsum is simply dummy text of the printing and typesetting industry. Lorem Ipsum has been the industry's standard dummy text ever since the 1500s.</p>
  <div class="foot"><span>© 2021 Corvath Therapeutics. All rights reserved</span><span>Page / 9</span></div>
</section>

<!-- Slide 10 : Team -->
<section class="slide col-r" style="top:1455px">
  <div class="brand" style="left:434px;top:10px"><span class="dot"></span>Corvath</div>
  <div class="ph p-lab" role="img" aria-label="Portrait of a team member in the lab" style="left:40px;top:49px;width:105px;height:132px"></div>
  <div class="ph p-sci" role="img" aria-label="Portrait of a team member at a microscope" style="left:150px;top:49px;width:105px;height:132px"></div>
  <div class="ph p-lab" role="img" aria-label="Portrait of a team member at a lab bench" style="left:259px;top:49px;width:105px;height:132px"></div>
  <p class="name" style="left:40px;top:191px;width:105px">Daniel Reyes</p>
  <p class="name" style="left:150px;top:191px;width:105px">Tomas Okafor</p>
  <p class="name" style="left:259px;top:191px;width:105px">Leo Marchetti</p>
  <p class="role" style="left:40px;top:203px;width:105px">Founder</p>
  <p class="role" style="left:150px;top:203px;width:105px">Founder</p>
  <p class="role" style="left:259px;top:203px;width:105px">Founder</p>
  <p class="body" style="left:44px;top:213px;width:97px;height:42px">Lorem Ipsum is simply dummy text of the printing and typesetting industry. Lorem Ipsum has been the industry's standard dummy text ever since</p>
  <p class="body" style="left:154px;top:213px;width:97px;height:42px">Lorem Ipsum is simply dummy text of the printing and typesetting industry. Lorem Ipsum has been the industry's standard dummy text ever since</p>
  <p class="body" style="left:263px;top:213px;width:97px;height:42px">Lorem Ipsum is simply dummy text of the printing and typesetting industry. Lorem Ipsum has been the industry's standard dummy text ever since</p>
  <h2 class="h2 caps" style="left:380px;top:51px;line-height:1.12">About<br>Corvath<br><span style="font-weight:400">Therapeutics</span><br>Team</h2>
  <p class="body" style="left:380px;top:132px;width:123px;height:120px">Lorem Ipsum is simply dummy text of the printing and typesetting industry. Lorem Ipsum has been the industry's standard dummy text ever since the 1500s, when an unknown printer took a galley of type and scrambled it to make a type specimen book. It has survived not only five centuries, but also the leap into electronic typesetting, remaining essentially unchanged. It is a long established fact that a reader will be distracted by the readable content</p>
  <div class="foot"><span>© 2021 Corvath Therapeutics. All rights reserved</span><span>Page / 10</span></div>
</section>

<!-- Slide 11 : Latest project -->
<section class="slide col-l" style="top:1795px">
  <div class="brand" style="left:37px;top:36px"><span class="dot"></span>Corvath</div>
  <h2 class="h2 caps" style="left:40px;top:72px">Our latest<br>project</h2>
  <div class="ph p-lab" role="img" aria-label="Scientist handling a sample at a lab bench" style="left:40px;top:113px;width:151px;height:153px"></div>
  <div class="num" style="left:204px;top:55px">I</div>
  <div class="num" style="left:204px;top:113px">II</div>
  <div class="num" style="left:204px;top:170px">III</div>
  <div class="num" style="left:204px;top:226px">IV</div>
  <p class="body" style="left:241px;top:55px;width:123px;height:40px">Lorem Ipsum is simply dummy text of the printing and typesetting industry. Lorem Ipsum has been the industry's standard dummy text ever since the 1500s.</p>
  <p class="body" style="left:241px;top:113px;width:123px;height:40px">Lorem Ipsum is simply dummy text of the printing and typesetting industry. Lorem Ipsum has been the industry's standard dummy text ever since the 1500s.</p>
  <p class="body" style="left:241px;top:170px;width:123px;height:40px">Lorem Ipsum is simply dummy text of the printing and typesetting industry. Lorem Ipsum has been the industry's standard dummy text ever since the 1500s.</p>
  <p class="body" style="left:241px;top:226px;width:123px;height:40px">Lorem Ipsum is simply dummy text of the printing and typesetting industry. Lorem Ipsum has been the industry's standard dummy text ever since the 1500s.</p>
  <div class="ph p-dish" role="img" aria-label="Culture dishes above a gloved hand pipetting" style="left:392px;top:40px;width:109px;height:225px"></div>
  <div class="foot"><span>© 2021 Corvath Therapeutics. All rights reserved</span><span>Page / 11</span></div>
</section>

<!-- Slide 12 : Latest project 2 -->
<section class="slide col-r" style="top:1795px">
  <div class="brand" style="left:37px;top:36px"><span class="dot"></span>Corvath</div>
  <h2 class="h2 caps" style="left:40px;top:72px">Our latest<br>project</h2>
  <ul class="bullets bold" style="left:40px;top:111px;font-size:7.5px"><li>Dummy text ever since</li><li>Readable content</li></ul>
  <p class="body" style="left:44px;top:146px;width:123px;height:110px">Lorem Ipsum is simply dummy text of the printing and typesetting industry. Lorem Ipsum has been the industry's standard dummy text ever since the 1500s, when an unknown printer took a galley of type and scrambled it to make a type specimen book. It has survived not only five centuries, but also the leap into electronic typesetting, remaining essentially unchanged. It is a long established fact that a reader will</p>
  <div class="ph p-couple" role="img" aria-label="Older couple embracing outdoors above culture dishes" style="left:191px;top:40px;width:125px;height:224px"></div>
  <p class="body" style="left:340px;top:38px;width:160px;height:64px">Lorem Ipsum is simply dummy text of the printing and typesetting industry. Lorem Ipsum has been the industry's standard dummy text ever since the 1500s, when an unknown printer took a galley of type and scrambled it to make a type specimen book. It has survived not only five centuries</p>
  <p class="body" style="left:340px;top:119px;width:160px;height:64px">Lorem Ipsum is simply dummy text of the printing and typesetting industry. Lorem Ipsum has been the industry's standard dummy text ever since the 1500s, when an unknown printer took a galley of type and scrambled it to make a type specimen book. It has survived not only five centuries</p>
  <p class="body" style="left:340px;top:196px;width:160px;height:64px">Lorem Ipsum is simply dummy text of the printing and typesetting industry. Lorem Ipsum has been the industry's standard dummy text ever since the 1500s, when an unknown printer took a galley of type and scrambled it to make a type specimen book. It has survived not only five centuries</p>
  <div class="foot"><span>© 2021 Corvath Therapeutics. All rights reserved</span><span>Page / 12</span></div>
</section>

</body>
</html>
```